full stationary design for a modern sleek design company

we are a design company that does modern minimalistic interior design works as well as other design services for high end clients.
we need a full stationary design including and not limited to (double sided business card, letter head, envelopes, documents folder...etc) that reflects the modern style design we do.
sleek modern and minimalistic is the requirements.
Updates

please use the latest attached files as there was a slight modification on the logo Added Wednesday, March 1, 2017

minor update on the logo files in JPG and PSD has been updated kindly follow the new attachments. Added Thursday, March 2, 2017

Target Market(s)

modern minimalist clients

Industry/Entity Type

Design Agency

Requirements
Must have
• the logo
Nice to have
• i like the colors in the colored 3D logo attached
Should not have
• too many colors

```html
<!DOCTYPE html>
<html lang="en">
<head>
<meta charset="utf-8">
<title>Linea Studio – Business Card</title>
<link href="https://fonts.googleapis.com/css2?family=Open+Sans:wght@400;600;700&display=swap" rel="stylesheet">
<style>
  :root {
    --backdrop: #e6e4e1;
    --card: #ffffff;
    --ink: #3a3a3a;
    --ink-soft: #4a4a4a;
    --accent: #f7941d;
    --charcoal: #3b3b3d;
    --render-dark: #2f2f31;
    --render-mid: #6d6d70;
    --render-light: #d9d9d9;
  }
  * { margin: 0; padding: 0; box-sizing: border-box; }
  html, body {
    width: 1200px; height: 987px; overflow: hidden;
    background: var(--backdrop);
    font-family: "Open Sans", Arial, sans-serif;
  }
  .canvas { position: relative; width: 1200px; height: 987px; }

  .card {
    position: absolute; left: 292px; width: 615px; height: 349px;
    background: var(--card); overflow: hidden;
  }
  .card--front { top: 131px; }
  .card--back { top: 506px; }

  .brand {
    position: absolute; top: 44px; right: 36px;
    display: flex; align-items: center; gap: 12px;
  }
  .brand__square { width: 30px; height: 30px; background: var(--accent); }
  .brand__name {
    font-weight: 700; font-size: 31px; letter-spacing: 1px;
    color: var(--charcoal); text-transform: uppercase; line-height: 1;
  }

  .holder { position: absolute; left: 32px; top: 176px; right: 36px; }
  .holder__name {
    font-weight: 600; font-size: 21px; color: var(--accent);
    text-transform: uppercase; line-height: 1.1;
  }
  .holder__role-row { display: flex; align-items: center; gap: 2px; margin-top: 2px; }
  .holder__role { font-size: 15px; color: var(--ink); white-space: nowrap; }
  .holder__rule { flex: 1; height: 1px; background: var(--ink); margin-top: 2px; }

  .contacts {
    position: absolute; left: 32px; top: 236px; list-style: none;
    font-size: 15px; color: var(--ink-soft);
  }
  .contacts li { display: flex; align-items: center; gap: 8px; height: 23.5px; }
  .contacts svg { width: 14px; height: 14px; fill: var(--accent); flex: none; }

  .address {
    position: absolute; right: 36px; top: 259px; text-align: right;
    font-size: 15px; line-height: 23.5px; color: var(--ink-soft); font-style: normal;
  }

  .bands { position: absolute; left: 0; bottom: 0; width: 615px; height: 25px; }
  .bands__dark { fill: var(--charcoal); }
  .bands__accent { fill: var(--accent); }
  .website {
    position: absolute; right: 20px; bottom: 3px;
    font-size: 15px; letter-spacing: 2.2px; color: #fff;
  }

  .render {
    width: 100%; height: 100%;
    background:
      linear-gradient(90deg, transparent 66%, var(--render-light) 66%),
      linear-gradient(180deg, var(--render-mid) 0%, var(--render-dark) 100%);
  }
</style>
</head>
<body>
<main class="canvas">
  <section class="card card--front">
    <div class="brand">
      <span class="brand__square"></span>
      <span class="brand__name">Linea Studio</span>
    </div>

    <div class="holder">
      <h1 class="holder__name">Daniel Reyes</h1>
      <div class="holder__role-row">
        <span class="holder__role">CEO&amp;Founder</span>
        <span class="holder__rule"></span>
      </div>
    </div>

    <ul class="contacts">
      <li>
        <svg viewBox="0 0 24 24" aria-hidden="true"><path d="M6.6 10.8a15.1 15.1 0 0 0 6.6 6.6l2.2-2.2a1 1 0 0 1 1-.25 11.4 11.4 0 0 0 3.6.57 1 1 0 0 1 1 1V20a1 1 0 0 1-1 1A17 17 0 0 1 3 4a1 1 0 0 1 1-1h3.5a1 1 0 0 1 1 1c0 1.25.2 2.45.57 3.57a1 1 0 0 1-.25 1z"/></svg>
        (555) 214 7730
      </li>
      <li>
        <svg viewBox="0 0 24 24" aria-hidden="true"><path d="M7 1h10a2 2 0 0 1 2 2v18a2 2 0 0 1-2 2H7a2 2 0 0 1-2-2V3a2 2 0 0 1 2-2zm0 3v14h10V4zm5 15.5a1.2 1.2 0 1 0 0 2.4 1.2 1.2 0 0 0 0-2.4z"/></svg>
        (555) 380 6142
      </li>
      <li>
        <svg viewBox="0 0 24 24" aria-hidden="true"><path d="M2 5h20v14H2zm2 2v.4l8 5 8-5V7zm0 2.8V17h16V9.8l-8 5z"/></svg>
        daniel@lineastudio.com
      </li>
    </ul>

    <address class="address">
      2140 Birchwood Avenue<br>
      Fairview, Oregon 97024
    </address>

    <svg class="bands" viewBox="0 0 615 25" aria-hidden="true">
      <polygon class="bands__dark" points="0,3 345,3 338,11 0,11"/>
      <polygon class="bands__accent" points="0,15 334,15 334,25 0,25"/>
      <polygon class="bands__accent" points="354,0 615,0 615,25 333,25"/>
    </svg>
    <span class="website">www.lineastudio.com</span>
  </section>

  <section class="card card--back">
    <div class="render" role="img" aria-label="3D interior render of a modern studio office with desks, computers, wall shelves and a white brick reception wall"></div>
  </section>
</main>
</body>
</html>
```